RK Cooling (logo) - Celebrating 55 Years Servicing the Chicago Suburbs. Summer is Almost Here! Make sure your system is running properly and efficiently. The industry standard recommends an A/C Clean & Check once a year.
A/C Clean & Check
Regular Preventive Maintenance Can:
-Help Prolong the Life of your Equipment
-Help Lower Your Monthly Energy Costs
-Save Costs on Future Repairs

Mention this Postcard and Take $10.00 Off
Call (555) 384-9120 I Address: 718 Birchwood Ave. Marvale, IL
_______________________________________________
BACK SIDE:
Proudly Serving Chicagoland Area Since 1961- We Also Service and Sell:
-Coastline Prime Equipment.
-Brightvane Air Cleaners & Humidifier Systems.
-Hot Water Heaters, Boilers, and Digital Thermostats.
-Residential and Commercial Fabrication. Custom Welding.

Schedule Your Spring Clean & Check Today
Phone: (555) 384-9120
Mail: rkcooling@mailnest.example
Website: www.rkcoolingair.example

I had pixel guild make a Fall Clean and Check (for furnaces) in September of 2015. Feel free too look back for ideas. The postcard needs to be creative and not the same as the fall one! Added Tuesday, March 29, 2016

Target Market(s)

HVAC Industry, Residential

Industry/Entity Type

Air Conditioning

Colors
0255a3
f6faec

Requirements
Must have
• The following text in the project description. Feel free to add more.
Nice to have
• One small picture or clipart on the front. Maybe a picture of something summery or an air conditioner.
Should not have
• No spelling mistakes. Nothing too basic.

```html
<!DOCTYPE html>
<html lang="en">
<head>
<meta charset="utf-8">
<title>RK Cooling – Summer Clean &amp; Check Postcard</title>
<link rel="stylesheet" href="https://fonts.googleapis.com/css2?family=Oswald:wght@500;700&family=Roboto+Condensed:wght@400;700;900&family=Open+Sans:ital,wght@1,600&display=swap">
<style>
  :root {
    --navy: #1d2a5a;
    --brand-blue: #0255a3;
    --sky: #1b8fd6;
    --bright: #29abe2;
    --cream: #f6faec;
    --ink: #2e2e2e;
    --white: #ffffff;
    --mist: #e4e8ee;
  }
  * { box-sizing: border-box; margin: 0; padding: 0; }
  html, body { width: 881px; height: 1200px; overflow: hidden; background: var(--white); }
  body { position: relative; font-family: "Roboto Condensed", "Arial Narrow", sans-serif; }

  .postcard {
    position: absolute; left: 34px; width: 792px; height: 540px;
    overflow: hidden; box-shadow: 0 2px 8px rgba(0,0,0,.25);
  }
  .postcard--front { top: 33px; background: var(--white); }
  .postcard--back {
    top: 596px;
    background: linear-gradient(160deg, #dff0ea 0%, #f3f8fa 35%, #e3edf5 60%, #c9dcea 100%);
  }

  .hero-photo {
    position: absolute; left: 0; top: 204px; width: 792px; height: 336px;
    background:
      radial-gradient(ellipse at 22% 55%, #e9ddd2 0%, rgba(233,221,210,0) 35%),
      linear-gradient(180deg, #e8c67a 0%, #d9b46a 30%, #a9b86c 60%, #7fa548 100%);
  }
  .front-shapes { position: absolute; left: 0; top: 0; }

  .brand-name {
    font-family: "Oswald", sans-serif; font-weight: 700; color: var(--navy);
    letter-spacing: .5px; line-height: 1; display: flex; align-items: center; gap: 8px;
  }
  .brand-name .mark { width: 14px; height: 14px; border-radius: 50%; background: var(--bright); }

  .front-logo { position: absolute; left: 24px; top: 30px; width: 250px; text-align: center; }
  .front-logo .brand-name { font-size: 44px; justify-content: center; }
  .tagline {
    margin-top: 10px; font-family: "Open Sans", sans-serif; font-style: italic; font-weight: 600;
    font-size: 14px; line-height: 1.45; color: var(--navy);
  }
  .tagline em { color: var(--sky); }

  .offer {
    position: absolute; left: 374px; top: 24px; font-family: "Roboto Condensed", sans-serif;
    font-weight: 700; font-size: 21px; color: var(--sky);
  }
  .summer-note {
    position: absolute; left: 358px; top: 80px; width: 410px; color: var(--white);
    font-weight: 700; font-size: 16.5px; line-height: 1.4;
  }

  .headline { position: absolute; left: 400px; top: 236px; width: 370px; text-align: center; }
  .headline .line { font-weight: 900; font-size: 34px; color: var(--ink); letter-spacing: .3px; line-height: 1; }
  .headline .cool {
    font-family: "Oswald", sans-serif; font-weight: 700; font-size: 118px; line-height: 1;
    color: var(--sky); -webkit-text-stroke: 3px var(--white); paint-order: stroke fill;
    margin: 4px 0 6px; letter-spacing: 2px;
  }
  .front-phone {
    position: absolute; left: 408px; top: 445px; width: 370px; text-align: center;
    font-weight: 700; font-size: 54px; color: var(--sky);
    -webkit-text-stroke: 2px var(--white); paint-order: stroke fill;
  }

  .back-curve { position: absolute; left: 0; top: 0; }
  .back-info { position: absolute; left: 26px; top: 26px; width: 330px; }
  .back-info .brand-name { font-size: 44px; justify-content: center; }
  .since { margin-top: 14px; text-align: center; color: var(--sky); font-weight: 700; font-size: 14px; }
  .section-title { color: var(--sky); font-weight: 700; font-size: 13.5px; text-transform: uppercase; margin-top: 16px; }
  .since + .section-title { margin-top: 18px; }
  .list { list-style: none; color: #111; font-weight: 700; font-size: 13.5px; line-height: 1.4; }
  .list .indent { padding-left: 6px; }
  .cta { margin-top: 16px; color: var(--sky); font-weight: 700; font-size: 17px; line-height: 1.3; text-transform: uppercase; }
  .contact { list-style: none; margin-top: 6px; color: #111; font-weight: 700; }
  .contact li { display: flex; align-items: center; gap: 6px; line-height: 1.5; }
  .contact .phone { font-size: 20px; }
  .contact .small { font-size: 14px; }
  .contact svg { flex: none; }

  .return-address {
    position: absolute; left: 408px; top: 56px; font-family: Arial, sans-serif;
    font-size: 13px; line-height: 1.45; color: #222; font-style: normal;
  }
</style>
</head>
<body>

<section class="postcard postcard--front">
  <div class="hero-photo" role="img" aria-label="Photo of a smiling family of four in white shirts outdoors, with a sunny meadow and houses behind them"></div>

  <svg class="front-shapes" width="792" height="540" viewBox="0 0 792 540" aria-hidden="true">
    <path d="M0,0 H792 V214 C640,206 470,190 300,204 L0,204 Z" fill="var(--white)"/>
    <path d="M300,204 C470,186 640,200 792,226 V248 C640,222 470,206 300,214 Z" fill="var(--mist)"/>
    <path d="M290,92 C420,62 600,72 792,32 V212 C640,198 470,176 290,200 Z" fill="var(--navy)"/>
    <path d="M0,0 H346 C340,140 220,226 0,196 Z" fill="var(--white)"/>
    <path d="M346,0 C340,140 220,226 0,196" fill="none" stroke="var(--bright)" stroke-width="14"/>
  </svg>

  <div class="front-logo">
    <div class="brand-name"><span class="mark"></span>RK COOLING</div>
    <p class="tagline">Celebrating <em>55 YEARS</em> Servicing<br>the Chicago Suburbs.</p>
  </div>

  <p class="offer">Mention this Postcard &amp; Take $10.00 OFF</p>
  <p class="summer-note">SUMMER IS ALMOST HERE! Make sure your system is running properly and efficiently. The industry standard recommends an A/C Clean &amp; Check once a year.</p>

  <div class="headline">
    <p class="line">KEEP YOUR FAMILY</p>
    <p class="cool">COOL</p>
    <p class="line">FOR THE SUMMER</p>
  </div>
  <p class="front-phone">(555) 384-9120</p>
</section>

<section class="postcard postcard--back">
  <svg class="back-curve" width="792" height="540" viewBox="0 0 792 540" aria-hidden="true">
    <path d="M356,0 C372,150 368,320 268,495 L298,495 C384,330 388,150 364,0 Z" fill="var(--navy)"/>
  </svg>

  <div class="back-info">
    <div class="brand-name"><span class="mark"></span>RK COOLING</div>
    <p class="since">Proudly Serving Chicagoland Area Since 1961</p>

    <p class="section-title">We also service and sell:</p>
    <ul class="list">
      <li>-Coastline Prime Equipment.</li>
      <li>-Brightvane Air Cleaners &amp; Humidifier Systems.</li>
      <li>-Hot Water Heaters, Boilers, and Digital Thermostats.</li>
      <li>-Residential and Commercial Fabrication,</li>
      <li class="indent">Custom Welding.</li>
    </ul>

    <p class="section-title">A/C Clean &amp; Check</p>
    <ul class="list">
      <li>Regular Preventive Maintenance Can:</li>
      <li>-Help Prolong the Life of your Equipment</li>
      <li>-Help Lower Your Monthly Energy Costs</li>
      <li>-Save Costs on Future Repairs</li>
    </ul>

    <p class="cta">Schedule your spring<br>clean &amp; check today!</p>
    <ul class="contact">
      <li class="phone">
        <svg width="14" height="16" viewBox="0 0 24 24"><path fill="var(--sky)" d="M6.6 10.8a15 15 0 0 0 6.6 6.6l2.2-2.2c.3-.3.7-.4 1-.2 1.1.4 2.3.6 3.6.6.6 0 1 .4 1 1V20c0 .6-.4 1-1 1A17 17 0 0 1 3 4c0-.6.4-1 1-1h3.5c.6 0 1 .4 1 1 0 1.3.2 2.5.6 3.6.1.3 0 .7-.2 1z"/></svg>
        (555) 384-9120
      </li>
      <li class="small">
        <svg width="13" height="10" viewBox="0 0 13 10"><rect x=".5" y=".5" width="12" height="9" fill="none" stroke="var(--sky)"/><path d="M.5 .5 6.5 5.5 12.5 .5" fill="none" stroke="var(--sky)"/></svg>
        rkcooling@mailnest.example
      </li>
      <li class="small">
        <svg width="12" height="12" viewBox="0 0 12 12"><circle cx="6" cy="6" r="5.3" fill="none" stroke="var(--sky)"/><rect x="5.3" y="5" width="1.4" height="4" fill="var(--sky)"/><circle cx="6" cy="3.4" r=".8" fill="var(--sky)"/></svg>
        www.rkcoolingair.example
      </li>
    </ul>
  </div>

  <address class="return-address">
    RK Cooling<br>
    718 Birchwood Ave.<br>
    Marvale, IL 60999
  </address>
</section>

</body>
</html>
```